Breast Cancer Stickers

Hi,
i would like a of small design for a breast cancer awareness campaign. please check attached picture this is the size and font i want. these will be stickers. Then i would like a little pink ribbon after each dot. so there will be four design please find below colors, slogans, etc..
1 I PINK I CAN. (Off white Background, Light Pink Font)
Never give up.
2 PINK POWER. (Black Background, Bright Pink Font)
Theres Always hope
3 POSITIVELY PINK. ( Light Pink Background, Off white Font)
Stay Positive
4 TURN UP THE PINK. (Bright Pink Background, Black font)
fight on.
Campaign

```html
<!DOCTYPE html>
<html lang="en">
<head>
<meta charset="utf-8">
<title>Breast Cancer Awareness Stickers</title>
<link rel="stylesheet" href="https://fonts.googleapis.com/css2?family=Inter:wght@700;800&display=swap">
<style>
  :root {
    --off-white: #f5f8e6;
    --light-pink: #f08397;
    --black: #231f20;
    --bright-pink: #e8389a;
    --page: #eef0f2;
    --sticker-size: 371px;
  }
  html, body {
    margin: 0;
    padding: 0;
    width: 1200px;
    height: 900px;
    overflow: hidden;
    background: var(--page);
    font-family: "Inter", "Helvetica Neue", Arial, sans-serif;
  }
  .sticker-sheet {
    position: relative;
    width: 1200px;
    height: 900px;
  }
  .sticker {
    position: absolute;
    width: var(--sticker-size);
    height: var(--sticker-size);
    box-sizing: border-box;
  }
  .sticker--never-give-up   { left: 229px; top: 54px;  background: var(--off-white);   color: var(--light-pink);  padding: 108px 0 0 42px; }
  .sticker--pink-power      { left: 656px; top: 54px;  background: var(--black);       color: var(--bright-pink); padding: 108px 0 0 50px; }
  .sticker--positively-pink { left: 229px; top: 475px; background: var(--light-pink);  color: var(--off-white);   padding: 100px 0 0 29px; }
  .sticker--turn-up         { left: 656px; top: 475px; background: var(--bright-pink); color: var(--black);       padding: 74px 0 0 50px; }

  .slogan {
    margin: 0;
    font-weight: 800;
    font-size: 66px;
    line-height: 55px;
    letter-spacing: -1.5px;
  }
  .slogan__line { display: block; white-space: nowrap; }
  .sticker--positively-pink .slogan { letter-spacing: -1px; }

  .ribbon {
    display: inline-block;
    width: 30px;
    height: 62px;
    margin-left: 3px;
    vertical-align: -14px;
  }
  .ribbon path { fill: none; stroke: currentColor; stroke-width: 5.5; stroke-linecap: round; stroke-linejoin: round; }

  .tagline {
    margin: 6px 0 0 0;
    font-weight: 700;
    font-size: 21px;
    line-height: 24px;
    letter-spacing: -0.2px;
  }
  .sticker--never-give-up .tagline { margin-top: -2px; }
  .sticker--pink-power .tagline { margin-top: -2px; }
  .sticker--positively-pink .tagline { margin-top: 0; }
  .sticker--turn-up .tagline { margin-top: -4px; }
</style>
</head>
<body>
<main class="sticker-sheet">

  <section class="sticker sticker--never-give-up">
    <h2 class="slogan">
      <span class="slogan__line">I Pink</span>
      <span class="slogan__line">I Can.<svg class="ribbon" viewBox="0 0 30 62" aria-hidden="true"><path d="M9 58 L19 30 C23 20 22 5 16 5 C10 5 9 20 13 30 L24 58"/></svg></span>
    </h2>
    <p class="tagline">Never give up.</p>
  </section>

  <section class="sticker sticker--pink-power">
    <h2 class="slogan">
      <span class="slogan__line">Pink</span>
      <span class="slogan__line">Power.<svg class="ribbon" viewBox="0 0 30 62" aria-hidden="true"><path d="M9 58 L19 30 C23 20 22 5 16 5 C10 5 9 20 13 30 L24 58"/></svg></span>
    </h2>
    <p class="tagline">There’s always hope.</p>
  </section>

  <section class="sticker sticker--positively-pink">
    <h2 class="slogan">
      <span class="slogan__line">positively</span>
      <span class="slogan__line">pink.<svg class="ribbon" viewBox="0 0 30 62" aria-hidden="true"><path d="M9 58 L19 30 C23 20 22 5 16 5 C10 5 9 20 13 30 L24 58"/></svg></span>
    </h2>
    <p class="tagline">Stay positive.</p>
  </section>

  <section class="sticker sticker--turn-up">
    <h2 class="slogan">
      <span class="slogan__line">Turn</span>
      <span class="slogan__line">Up the</span>
      <span class="slogan__line">Pink.<svg class="ribbon" viewBox="0 0 30 62" aria-hidden="true"><path d="M9 58 L19 30 C23 20 22 5 16 5 C10 5 9 20 13 30 L24 58"/></svg></span>
    </h2>
    <p class="tagline">Fight on.</p>
  </section>

</main>
</body>
</html>
```